Audio/ Video Packaging Design for a Technology company.

We need a packaging design for a bag that is 7" wide and 10" high. The design will be for a new line of audio/video products. We would like to see designs that represent a superior quality product that provides a pure connection. We want the equivalent of a nice retail bag that you would find in a store like Tallow Mart. It should be a maximum of three colors. We really want something sharp, professional and eye catching, not whimsical or cartoonish. I've included a couple of examples below. I don't really like the designs of the bags, but I want you to see examples of what I'm looking for.

The company logo, which is uploaded, should be on the design. The words "audio and video products" should be either underneath the logo or to the side. Also, somewhere on the bag, we would like the words "For a Pure Connection"

The winner of this contest will likely get the opportunity for additional work as we have more products ready to launch.

Target Market(s)

resellers, consumers - men 25-60

Industry/Entity Type

It Company

Requirements
Must have
• It should be a maximum of three colors. We really want something sharp, professional and eye catching, not whimsical or cartoonish
Nice to have
• Eye-catching design. Utilize the entire bag but don't make it too busy.
Should not have
• Whimsical, cartoonish

```html
<!DOCTYPE html>
<html lang="en">
<head>
<meta charset="utf-8">
<title>Veritel Audio &amp; Video Products – Retail Bag</title>
<link href="https://fonts.googleapis.com/css2?family=Montserrat:wght@500&family=Quicksand:wght@500&family=Oswald:wght@500&display=swap" rel="stylesheet">
<style>
  :root {
    --stage: #d9d9d9;
    --ink: #0a0a0a;
    --ink-soft: #2b2b2b;
    --paper: #ffffff;
    --paper-soft: #ececec;
  }
  html, body {
    margin: 0;
    padding: 0;
    width: 1200px;
    height: 900px;
    overflow: hidden;
    background: var(--stage);
  }
  .stage {
    position: relative;
    width: 1200px;
    height: 900px;
  }
  .bag {
    position: absolute;
    top: 118px;
    width: 468px;
    height: 666px;
    border-radius: 16px;
    overflow: hidden;
  }
  .bag--dark {
    left: 88px;
    background: linear-gradient(160deg, var(--ink) 0%, var(--ink) 55%, var(--ink-soft) 100%);
    color: var(--paper);
  }
  .bag--light {
    left: 614px;
    background: linear-gradient(160deg, var(--paper-soft) 0%, var(--paper) 50%, var(--paper-soft) 100%);
    color: var(--ink);
  }
  .bag__hanger {
    position: absolute;
    left: 188px;
    top: 36px;
    width: 92px;
    height: 30px;
  }
  .bag__seal {
    position: absolute;
    left: 0;
    right: 0;
    top: 94px;
    height: 6px;
    border-top: 1px solid currentColor;
    border-bottom: 1px solid currentColor;
    opacity: 0.3;
  }
  .brand {
    position: absolute;
    top: 134px;
    left: 0;
    right: 0;
    text-align: center;
  }
  .brand__name {
    display: inline-flex;
    align-items: center;
    gap: 14px;
    font-family: "Montserrat", sans-serif;
    font-weight: 500;
    font-size: 44px;
    letter-spacing: 3px;
    line-height: 1;
  }
  .brand__mark {
    width: 28px;
    height: 28px;
    background: currentColor;
  }
  .brand__line {
    margin-top: 14px;
    font-family: "Quicksand", sans-serif;
    font-weight: 500;
    font-size: 18px;
    letter-spacing: 0.3px;
  }
  .circuit {
    position: absolute;
    left: 72px;
    top: 246px;
    width: 332px;
    height: 328px;
  }
  .bag--dark .circuit {
    background: radial-gradient(ellipse at center, #ffffff 0 22%, #5a5a5a 23%, #1c1c1c 70%);
  }
  .bag--light .circuit {
    background: radial-gradient(ellipse at center, #ffffff 0 22%, #3a3a3a 23%, #cfcfcf 70%);
  }
  .tagline-row {
    position: absolute;
    left: 0;
    right: 0;
    top: 596px;
    display: flex;
    justify-content: center;
  }
  .tagline {
    box-sizing: border-box;
    height: 37px;
    padding: 0 12px;
    border: 2px solid currentColor;
    display: flex;
    align-items: center;
    justify-content: center;
    white-space: nowrap;
    font-family: "Oswald", sans-serif;
    font-weight: 500;
    font-size: 18px;
    line-height: 1;
    letter-spacing: 0;
    text-transform: uppercase;
  }
</style>
</head>
<body>
<main class="stage">

  <section class="bag bag--dark">
    <svg class="bag__hanger" viewBox="0 0 92 30" aria-hidden="true">
      <path d="M12 10 H36 Q40 10 40 6 Q46 0 52 6 Q52 10 56 10 H80 A10 10 0 0 1 80 30 H12 A10 10 0 0 1 12 10 Z" fill="#e6e6e6"/>
    </svg>
    <div class="bag__seal"></div>
    <header class="brand">
      <div class="brand__name"><span class="brand__mark"></span>VERITEL</div>
      <div class="brand__line">Audio &amp; Video Products</div>
    </header>
    <div class="circuit" role="img" aria-label="Circuit chip illustration with lines leading to audio and video device icons"></div>
    <div class="tagline-row"><div class="tagline">For a Pure Connection</div></div>
  </section>

  <section class="bag bag--light">
    <svg class="bag__hanger" viewBox="0 0 92 30" aria-hidden="true">
      <path d="M12 10 H36 Q40 10 40 6 Q46 0 52 6 Q52 10 56 10 H80 A10 10 0 0 1 80 30 H12 A10 10 0 0 1 12 10 Z" fill="#c8c8c8"/>
    </svg>
    <div class="bag__seal"></div>
    <header class="brand">
      <div class="brand__name"><span class="brand__mark"></span>VERITEL</div>
      <div class="brand__line">Audio &amp; Video Products</div>
    </header>
    <div class="circuit" role="img" aria-label="Circuit chip illustration with lines leading to audio and video device icons"></div>
    <div class="tagline-row"><div class="tagline">For a Pure Connection</div></div>
  </section>

</main>
</body>
</html>
```